Bright Arrow Delivery Service Wordpress design

My client is a delivery service whose motto is "We go where the freight leads us." Their colors are red, white and blue. They use Voyalo vans and box vans - NO semi tractors. They like this Website design www.tovamu-sample.com, but I would like to see some designs that make them stand out. Attached is their new logo.

Target Market(s)

Businesses who use delivery services in town and anyone needing freight picked up or transported in the United States.

Industry/Entity Type

Delivery Service

Number of Pages Required

1 page

Font styles to use
Sans Serif

Colors
ec1f27
0455a3
ffffff

Requirements
Must have
• We need a Wordpress design with sliders that incorporates their new logo and the motto "WE GO WHERE THE FREIGHT LEADS US" Their corporate colors are red, white and blue. They only use voyalo vans and box vans.
Nice to have
• Please use your creativity to come up with a unique design for this delivery service.
Should not have
• NO SEMI TRACTOR TRAILERS

```html
<!DOCTYPE html>
<html lang="en">
<head>
<meta charset="utf-8">
<title>Bright Arrow Delivery Service</title>
<link rel="stylesheet" href="https://fonts.googleapis.com/css2?family=Open+Sans:ital,wght@0,400;0,600;0,700;0,800;1,400;1,600&family=Montserrat:wght@400;600;700&display=swap">
<style>
:root{
  --red:#ec1f27;
  --blue:#0455a3;
  --navy:#141a44;
  --navy-deep:#0d1233;
  --white:#ffffff;
  --grey-bg:#eef0f4;
  --text:#5b6070;
  --muted:#b9bdd2;
}
*{margin:0;padding:0;box-sizing:border-box}
html,body{width:1200px;height:2348px;overflow:hidden}
body{font-family:"Open Sans",Arial,sans-serif;color:var(--text);background:var(--white);position:relative}
.abs{position:absolute}

/* top bar */
.topbar{left:0;top:0;width:1200px;height:36px;background:var(--white)}
.topbar-contact{right:0;top:0;width:480px;height:36px;background:var(--red);
  clip-path:polygon(24px 0,100% 0,100% 100%,0 100%);display:flex;align-items:center;justify-content:flex-end;gap:28px;padding-right:28px;color:var(--white);font-size:13px;font-weight:600;white-space:nowrap}
.topbar-contact span{display:flex;align-items:center;gap:8px}

/* brand */
.brand{left:40px;top:46px;z-index:5;display:flex;align-items:center;gap:12px;background:var(--white);padding:10px 16px;border-radius:4px}
.brand-mark{width:22px;height:22px;background:var(--red);display:block}
.brand-name{font-weight:800;font-size:24px;color:var(--navy);letter-spacing:.5px}

/* hero */
.hero{left:0;top:36px;width:1200px;height:624px;background:linear-gradient(100deg,#c9ccd3 0%,#e6e8ec 35%,#aeb6c4 62%,#3b4a6e 100%)}
.nav{left:210px;top:152px;height:40px;display:flex;background:var(--white);z-index:4;box-shadow:0 2px 6px rgba(0,0,0,.15)}
.nav a{display:block;padding:0 18px;line-height:40px;font-family:"Montserrat",Arial,sans-serif;font-size:14px;font-weight:600;color:var(--navy);text-decoration:none}
.nav a.active{background:var(--navy);color:var(--white)}
.hero-panel{left:152px;top:296px;width:468px;height:262px;background:rgba(20,26,68,.82);border-radius:6px;padding:30px 32px;color:var(--white)}
.hero-panel h1{font-family:"Montserrat",Arial,sans-serif;font-size:29px;font-weight:700;line-height:1.2;letter-spacing:.3px}
.hero-panel h1 em{font-style:normal;color:var(--red)}
.hero-panel p{margin-top:16px;font-size:13px;line-height:1.55;color:#d8dbe8}
.btn-outline{margin-top:20px;display:inline-flex;align-items:center;gap:12px;border:1px solid var(--white);border-radius:3px;padding:9px 16px;font-size:13px;font-weight:700;letter-spacing:.5px}
.slider-arrow{top:442px;width:36px;height:40px;background:rgba(255,255,255,.75);display:flex;align-items:center;justify-content:center}

/* services */
.services{left:0;top:660px;width:1200px;height:488px;background:var(--grey-bg)}
.card{top:680px;width:286px;height:370px;background:var(--white);box-shadow:0 4px 14px rgba(0,0,0,.12);text-align:center;padding:40px 30px 0}
.card-icon{width:64px;height:64px;border-radius:50%;background:var(--red);margin:0 auto;display:flex;align-items:center;justify-content:center}
.card h3{margin-top:28px;font-family:"Montserrat",Arial,sans-serif;font-size:16px;font-weight:700;color:var(--navy);letter-spacing:.5px}
.card p{margin-top:14px;font-size:12px;line-height:1.6;color:var(--text)}
.btn-small{margin-top:26px;display:inline-block;border:1px solid #c7cad4;border-radius:3px;padding:7px 22px;font-size:12px;color:var(--navy);background:#f7f8fa}

/* testimonials */
.testimonials{left:0;top:1148px;width:1200px;height:432px;background:linear-gradient(135deg,#1b2256 0%,var(--navy) 50%,#10163c 100%)}
.section-title{width:1200px;text-align:center;font-family:"Montserrat",Arial,sans-serif;font-size:28px;font-weight:400}
.section-title em{font-style:italic;color:var(--red);font-weight:600}
.title-rule{width:1200px;display:flex;justify-content:center}
.avatar{left:220px;top:1336px;width:96px;height:96px;border-radius:50%;background:radial-gradient(circle at 50% 40%,#e9c3a4,#c98b5c 70%,#8a5a3a);border:4px solid var(--white)}
.quote-mark{font-family:Georgia,serif;font-size:64px;color:var(--white);line-height:1}
.quote-text{left:376px;top:1310px;width:540px;font-size:14px;line-height:1.65;color:#d9dcea;font-style:italic}
.quote-name{left:376px;top:1438px;font-size:16px;font-style:italic;font-weight:600;color:var(--white)}
.dots{top:1500px;left:0;width:1200px;display:flex;justify-content:center;gap:8px}
.dots i{width:10px;height:10px;border-radius:50%;background:#6c7196;display:block}
.dots i.on{background:var(--red)}

/* clients */
.client-box{top:1776px;width:244px;height:116px;background:var(--white);box-shadow:0 3px 12px rgba(0,0,0,.12);display:flex;align-items:center;justify-content:center;gap:10px}
.client-box span{font-weight:800;font-size:30px;color:var(--navy)}
.client-dot{width:14px;height:14px;background:var(--red);display:block}
.client-arrow{top:1814px;font-size:30px;color:#555;font-weight:700}

/* footer */
.footer{left:0;top:1988px;width:1200px;height:312px;background:var(--navy-deep)}
footer h4{font-family:"Montserrat",Arial,sans-serif;font-size:14px;font-weight:700;color:var(--white);letter-spacing:.5px}
.footer-links{list-style:none;margin-top:20px;font-size:13px;line-height:1.6;color:var(--muted)}
.footer-contact{margin-top:20px;font-size:13px;line-height:1.7;color:var(--muted)}
.footer-contact div{display:flex;gap:10px;align-items:flex-start;margin-bottom:6px}
.field{width:200px;height:30px;background:var(--white);margin-top:10px;font-size:12px;color:#888;padding:6px 10px}
.field.tall{height:64px}
.btn-submit{margin-top:12px;width:84px;height:30px;background:var(--red);color:var(--white);font-size:12px;font-weight:700;display:flex;align-items:center;justify-content:center;letter-spacing:.5px}
.footer-brand{left:60px;top:2092px;display:flex;align-items:center;gap:10px}
.footer-brand span{font-weight:800;font-size:22px;color:var(--white)}
.bottombar{left:0;top:2300px;width:1200px;height:48px;background:#080b22;color:var(--muted);font-size:11px;display:flex;align-items:center;justify-content:space-between;padding:0 40px}
.socials{display:flex;gap:6px}
.socials i{width:16px;height:16px;border-radius:50%;background:var(--white);display:block}
</style>
</head>
<body>

<header>
  <div class="abs hero" role="img" aria-label="Smiling courier in uniform unloading a cardboard parcel from a delivery van"></div>
  <div class="abs topbar"></div>
  <div class="abs topbar-contact">
    <span><svg width="14" height="14" viewBox="0 0 24 24"><path fill="#fff" d="M6.6 10.8a15 15 0 006.6 6.6l2.2-2.2a1 1 0 011-.25 11.4 11.4 0 003.6.57 1 1 0 011 1V20a1 1 0 01-1 1A17 17 0 013 4a1 1 0 011-1h3.5a1 1 0 011 1c0 1.25.2 2.45.57 3.57a1 1 0 01-.25 1z"/></svg>800.555.0142</span>
    <span><svg width="16" height="12" viewBox="0 0 16 12"><rect x="0.5" y="0.5" width="15" height="11" fill="none" stroke="#fff"/><path d="M1 1l7 6 7-6" fill="none" stroke="#fff"/></svg>info@brightarrow-sample.com</span>
  </div>
  <div class="abs brand"><i class="brand-mark"></i><span class="brand-name">BRIGHT ARROW</span></div>
  <nav class="abs nav">
    <a class="active">HOME</a><a>ABOUT</a><a>COURIER</a><a>MEDICAL</a><a>FREIGHT</a><a>CAREERS</a><a>CLIENTS</a><a>CONTACT</a>
  </nav>
  <div class="abs hero-panel">
    <h1>WE GO WHERE <em>THE FREIGHT</em> LEADS US</h1>
    <p>Lorem ipsum dolor sit amet, consectetuer adipiscing elit, sed diam nonummy nibh euismod tincidunt ut laoreet dolore magna aliquam erat volutpat. Duis autem vel eum iriure dolor in hendrerit.</p>
    <div class="btn-outline">LEARN MORE
      <svg width="18" height="18" viewBox="0 0 18 18"><circle cx="9" cy="9" r="8" fill="none" stroke="#fff"/><path d="M7.5 5.5L11 9l-3.5 3.5" fill="none" stroke="#fff" stroke-width="1.5"/></svg>
    </div>
  </div>
  <div class="abs slider-arrow" style="left:0"><svg width="12" height="16" viewBox="0 0 12 16"><path d="M9 2L3 8l6 6" fill="none" stroke="#333" stroke-width="2"/></svg></div>
  <div class="abs slider-arrow" style="right:0"><svg width="12" height="16" viewBox="0 0 12 16"><path d="M3 2l6 6-6 6" fill="none" stroke="#333" stroke-width="2"/></svg></div>
</header>

<section>
  <div class="abs services"></div>
  <article class="abs card" style="left:160px">
    <div class="card-icon"><svg width="34" height="34" viewBox="0 0 24 24"><path fill="#fff" d="M21 16v-2l-8-5V3.5a1.5 1.5 0 00-3 0V9l-8 5v2l8-2.5V19l-2 1.5V22l3.5-1 3.5 1v-1.5L13 19v-5.5z"/></svg></div>
    <h3>EXPRESS COURIER</h3>
    <p>Lorem ipsum dolor sit amet, consectetuer adipiscing elit, sed diam nonummy nibh euismod tincidunt ut laoreet dolore magna aliquam erat volutpat. Ut wisi enim ad minim veniam, quis nostrud.</p>
    <span class="btn-small">Learn More</span>
  </article>
  <article class="abs card" style="left:457px">
    <div class="card-icon"><svg width="34" height="34" viewBox="0 0 24 24"><rect x="3" y="7" width="18" height="13" rx="2" fill="#fff"/><rect x="9" y="4" width="6" height="4" rx="1" fill="none" stroke="#fff" stroke-width="1.6"/><path d="M11 10h2v3h3v2h-3v3h-2v-3H8v-2h3z" fill="#ec1f27"/></svg></div>
    <h3>MEDICAL COURIER</h3>
    <p>Lorem ipsum dolor sit amet, consectetuer adipiscing elit, sed diam nonummy nibh euismod tincidunt ut laoreet dolore magna aliquam erat volutpat. Ut wisi enim ad minim veniam, quis nostrud.</p>
    <span class="btn-small">Learn More</span>
  </article>
  <article class="abs card" style="left:754px">
    <div class="card-icon"><svg width="36" height="36" viewBox="0 0 24 24"><rect x="2" y="6" width="12" height="10" fill="#fff"/><path d="M14 9h4l3 3.5V16h-7z" fill="#fff"/><circle cx="6" cy="17.5" r="2" fill="#fff" stroke="#ec1f27"/><circle cx="17" cy="17.5" r="2" fill="#fff" stroke="#ec1f27"/></svg></div>
    <h3>EXPRESS FREIGHT</h3>
    <p>Lorem ipsum dolor sit amet, consectetuer adipiscing elit, sed diam nonummy nibh euismod tincidunt ut laoreet dolore magna aliquam erat volutpat. Ut wisi enim ad minim veniam, quis nostrud.</p>
    <span class="btn-small">Learn More</span>
  </article>
</section>

<section>
  <div class="abs testimonials" role="img" aria-label="Dim warehouse interior with stacked freight shelves under a navy tint"></div>
  <h2 class="abs section-title" style="left:0;top:1216px;color:var(--white)">Client <em>Testimonials</em></h2>
  <div class="abs title-rule" style="left:0;top:1262px"><svg width="60" height="10" viewBox="0 0 60 10"><rect y="1" width="60" height="3" fill="#ec1f27"/><rect y="6" width="60" height="3" fill="#0455a3"/></svg></div>
  <div class="abs avatar" role="img" aria-label="Client portrait"></div>
  <div class="abs quote-mark" style="left:334px;top:1300px">&ldquo;</div>
  <p class="abs quote-text">Lorem ipsum dolor sit amet, consectetuer adipiscing elit, sed diam nonummy nibh euismod tincidunt ut laoreet dolore magna aliquam erat volutpat. Ut wisi enim ad minim veniam, quis nostrud exerci tation ullamcorper suscipit lobortis nisl ut aliquip ex ea commodo consequat.</p>
  <div class="abs quote-mark" style="left:920px;top:1380px">&rdquo;</div>
  <p class="abs quote-name">Marlene Tovar</p>
  <div class="abs dots"><i></i><i class="on"></i><i></i></div>
</section>

<section>
  <h2 class="abs section-title" style="left:0;top:1636px;color:var(--navy)">Our <em>Clients</em></h2>
  <div class="abs title-rule" style="left:0;top:1682px"><svg width="60" height="10" viewBox="0 0 60 10"><rect y="1" width="60" height="3" fill="#ec1f27"/><rect y="6" width="60" height="3" fill="#0455a3"/></svg></div>
  <div class="abs client-arrow" style="left:38px">&lsaquo;</div>
  <div class="abs client-box" style="left:82px"><span>NORVEXA</span></div>
  <div class="abs client-box" style="left:346px"><i class="client-dot"></i><span>KELBRIN</span></div>
  <div class="abs client-box" style="left:610px"><span>TRAMWELL</span></div>
  <div class="abs client-box" style="left:874px"><span>OSTRADA</span></div>
  <div class="abs client-arrow" style="left:1150px">&rsaquo;</div>
</section>

<footer>
  <div class="abs footer"></div>
  <div class="abs footer-brand"><i class="brand-mark"></i><span>BRIGHT ARROW</span></div>
  <div class="abs" style="left:384px;top:2024px">
    <h4>QUICK LINKS</h4>
    <ul class="footer-links"><li>Home</li><li>About</li><li>Courier</li><li>Medical</li><li>Freight</li><li>Careers</li><li>Clients</li><li>Contact</li></ul>
  </div>
  <div class="abs" style="left:552px;top:2024px;width:250px">
    <h4>CONTACT</h4>
    <div class="footer-contact">
      <div><svg width="12" height="16" viewBox="0 0 12 16"><path d="M6 0a6 6 0 016 6c0 4.5-6 10-6 10S0 10.5 0 6a6 6 0 016-6z" fill="#ec1f27"/><circle cx="6" cy="6" r="2" fill="#0d1233"/></svg><span>Bright Arrow Express Delivery<br>48 Harbor Lane<br>Fairhaven, CA 90000</span></div>
      <div><svg width="12" height="12" viewBox="0 0 24 24"><path fill="#ec1f27" d="M6.6 10.8a15 15 0 006.6 6.6l2.2-2.2a1 1 0 011-.25 11.4 11.4 0 003.6.57 1 1 0 011 1V20a1 1 0 01-1 1A17 17 0 013 4a1 1 0 011-1h3.5a1 1 0 011 1c0 1.25.2 2.45.57 3.57a1 1 0 01-.25 1z"/></svg><span>1.800.555.0142</span></div>
      <div><svg width="14" height="10" viewBox="0 0 16 12"><rect x="0.5" y="0.5" width="15" height="11" fill="none" stroke="#ec1f27"/><path d="M1 1l7 6 7-6" fill="none" stroke="#ec1f27"/></svg><span>info@brightarrow-sample.com</span></div>
    </div>
  </div>
  <div class="abs" style="left:830px;top:2024px">
    <h4>SEND A MESSAGE</h4>
    <div class="field" style="margin-top:20px">Name</div>
    <div class="field">Email</div>
    <div class="field tall">Message</div>
    <div class="btn-submit">SUBMIT</div>
  </div>
  <div class="abs bottombar">
    <span>COPYRIGHT &copy; 2016 BRIGHT ARROW EXPRESS DELIVERY. ALL RIGHTS RESERVED.</span>
    <span class="socials"><i></i><i></i><i></i><i></i></span>
  </div>
</footer>

</body>
</html>
```